Resident Guide for Senior Living Community

I need to create an informational magazine for residents that live in an Assisted Living community. This magazine is designed to educate the resident about the different service options and features that the community provides. I don't want to use any of the pictures in the Word Document - please use the uploaded picture instead. The final design should be both informational and elegant. The text in the word document is the actual text that needs to be used in the Resident Guide. Thanks!

Target Market(s)

Senior citizens and adult children (55 - 65 years old)

Industry/Entity Type

Assisted Living

Requirements
Must have
• Must be elegant - think Vellmore Orsay. Needs to have a lot of pictures and the logo must be used. The logo is the Plaque that says The Pellow Court.
Nice to have
• The Word doucment is the old Resident Guide - we are looking for a refresh using the same content.
Should not have
• please do not use any pictures from the Word Document other than the Logo.

```html
<!DOCTYPE html>
<html lang="en">
<head>
<meta charset="utf-8">
<title>Our Pledge — Resident Guide Spread</title>
<link href="https://fonts.googleapis.com/css2?family=Playfair+Display:ital,wght@0,400;0,500;1,400&family=Libre+Baskerville:ital@0;1&display=swap" rel="stylesheet">
<style>
  :root {
    --backdrop: #ab9c90;
    --paper: #ffffff;
    --ink: #2a2624;
    --headline: #ffffff;
    --dropcap: #dcd6d2;
    --photo-warm: #b9a08c;
    --photo-rose: #e4c9bd;
    --photo-dark: #1c1716;
    --photo-navy: #2e3a5c;
  }
  * { margin: 0; padding: 0; box-sizing: border-box; }
  html, body { width: 1200px; height: 800px; overflow: hidden; }
  body {
    background: var(--backdrop);
    display: flex; align-items: center; justify-content: center;
  }
  .spread {
    position: relative;
    width: 1080px; height: 700px;
    background: var(--paper);
    box-shadow: 0 18px 40px rgba(0,0,0,.25);
    overflow: hidden;
  }
  .spread-photo {
    position: absolute; left: 0; top: 0;
    width: 820px; height: 100%;
    background:
      linear-gradient(180deg, rgba(0,0,0,0) 55%, rgba(20,16,16,.55) 100%),
      linear-gradient(90deg, var(--photo-warm) 0%, #c9b7ad 22%, var(--photo-navy) 40%, var(--photo-dark) 52%, var(--photo-rose) 66%, #d9b8a6 80%, var(--photo-dark) 100%);
  }
  .gutter {
    position: absolute; left: 539px; top: 0; width: 2px; height: 100%;
    background: linear-gradient(90deg, rgba(0,0,0,.25), rgba(0,0,0,0));
  }
  .headline {
    position: absolute; left: 440px; top: 470px;
    width: 370px;
    font-family: "Playfair Display", serif;
    font-weight: 400;
    color: var(--headline);
    line-height: 1;
    white-space: nowrap;
  }
  .headline-title {
    display: block;
    font-size: 66px; font-weight: 400; letter-spacing: -0.5px;
    text-align: right;
  }
  .headline-sub {
    display: block;
    font-style: italic;
    font-weight: 400;
    font-size: 23px;
    margin-top: 8px;
    text-align: right;
  }
  .pledge-column {
    position: absolute; left: 838px; top: 160px; width: 210px;
    font-family: "Libre Baskerville", serif;
    font-style: italic;
    font-size: 8.6px; line-height: 1.5;
    color: var(--ink);
  }
  .pledge-column p { margin-bottom: 9px; }
  .dropcap {
    position: absolute; left: -14px; top: -30px;
    font-family: "Playfair Display", serif;
    font-style: italic;
    font-size: 72px; color: var(--dropcap);
    line-height: 1;
  }
  .pledge-lead { padding-left: 28px; position: relative; }
  .pledge-credit { margin-top: 14px; }
  .signature {
    width: 150px; height: 34px; margin-top: 28px;
    background: linear-gradient(90deg, #e8e4e1, #f4f2f0);
    border-radius: 3px;
  }
</style>
</head>
<body>
  <main class="spread">
    <div class="spread-photo" role="img" aria-label="Portrait of the community's founders in an elegant parlour beside a grand piano and a vase of fresh flowers"></div>
    <div class="gutter"></div>

    <h1 class="headline">
      <span class="headline-title">Our Pledge.</span>
      <span class="headline-sub">To Our Families and Residents.</span>
    </h1>

    <article class="pledge-column">
      <span class="dropcap" aria-hidden="true">W</span>
      <p class="pledge-lead">We promise to devote our love, strength and understanding daily to bring as much happiness, confidence, self-esteem, security and well being as possible to our family of residents. We understand that the real value of our care giving is not measured by our education and credentials or even by our years of experience. It is rather the amount of heart and giving of ourselves which we willingly share with our resident family members.</p>
      <p>We pledge to create in our homes an atmosphere of friendship, care and love, realizing that an unexpected hug, a gentle taking of a hand or a whispered compliment can do more good and bring more joy than we can imagine.</p>
      <p>We dedicate and commit ourselves to offering a quality of care and service to our residents which will only be second to the family's or special friend's love and concern.</p>
      <p>With the help of a devoted, loving and dedicated management and staff, the family's and special friend's interest and love, and with the protection and guidance of God, we make this pledge to each resident and to his/her family and friends.</p>
      <p class="pledge-credit">Composed for the opening of<br>The Pellow Court Alder Springs in 1988</p>
      <div class="signature" role="img" aria-label="Founder's handwritten signature"></div>
    </article>
  </main>
</body>
</html>
```